Whitepaper: 7 Keys to Achieving Success of Your RTLS Initiative

Create a graphical layout for a whitepaper that would include 7 illustrations matching each subject line. Colors aligned with Boundless Stride branding guide (attached)
Updates

Just to summarize, I would need graphics/illustrations for 7 bullet points - Key #1: Set Measurements for Success Key #2: Establish a Clear Roadmap Key #3: Don’t Use Pilots (small try out of software) Key #4: Plan for the Future, from the Start Key #5: Think about RTLS as an Initiative, not a Project Key #6: Nurture the Change Key #7: Show Successes, Early

I would expect about 2-3 illustrations per page. Format - US size 8.5x11. PDF file, but would like to have the ability to edit text if needed. Thank you for your interest. Colors don't need to match the branding. It is a healthcare whitepaper so it could be blue and green.

Project Deadline Extended
Reason: Some of you have asked for a time extension.

```html
<!DOCTYPE html>
<html lang="en">
<head>
<meta charset="utf-8">
<title>7 Keys to Achieving Success of Your RTLS Initiative</title>
<link href="https://fonts.googleapis.com/css2?family=Rubik:wght@500;600&family=Didact+Gothic&display=swap" rel="stylesheet">
<style>
  :root {
    --backdrop: #e4e4e4;
    --paper: #ffffff;
    --coral: #f0625e;
    --coral-soft: #fbe1df;
    --ink: #2f323a;
    --body: #4b4b4f;
    --rule: #c9c9cc;
    --footer: #3d4049;
    --footer-text: #f2f2f2;
  }
  * { box-sizing: border-box; margin: 0; padding: 0; }
  html, body { width: 1200px; height: 793px; overflow: hidden; background: var(--backdrop); }
  .spread { position: relative; width: 1200px; height: 793px; }
  .page {
    position: absolute; width: 518px; height: 671px; background: var(--paper);
    font-family: "Didact Gothic", sans-serif; color: var(--body); overflow: hidden;
  }
  .page--left { left: 72px; top: 64px; }
  .page--right { left: 620px; top: 62px; }

  .page-header { position: absolute; left: 66px; top: 42px; width: 388px; height: 30px; }
  .brand {
    position: absolute; left: 0; top: 6px; font-family: "Rubik", sans-serif; font-weight: 500;
    font-size: 16px; color: var(--ink); letter-spacing: -0.2px; white-space: nowrap;
  }
  .header-rule { position: absolute; left: 102px; right: 0; top: 24px; border-top: 1px solid var(--rule); }
  .header-title {
    position: absolute; right: 0; top: 13px; font-family: "Rubik", sans-serif; font-weight: 500;
    font-size: 5.6px; color: var(--ink);
  }

  .key { position: absolute; left: 66px; width: 388px; }
  .key-art {
    position: absolute; left: 0; top: 0; width: 62px; height: 66px;
    background: var(--coral-soft); border-radius: 4px;
  }
  .key-label {
    position: absolute; left: 79px; top: 0; height: 26px; padding: 0 9px; border-radius: 13px;
    background: var(--coral); color: #fff; font-family: "Rubik", sans-serif; font-weight: 500;
    font-size: 13px; line-height: 26px;
  }
  .key-title {
    position: absolute; left: 79px; top: 34px; width: 320px; font-family: "Rubik", sans-serif;
    font-weight: 600; font-size: 16px; line-height: 20px; color: var(--ink);
  }
  .key-text {
    position: absolute; left: 0; width: 388px; font-size: 9.6px; line-height: 17.3px; color: var(--body);
  }

  .page-number {
    position: absolute; left: 404px; top: 595px; width: 46px; height: 46px; border-radius: 50%;
    background: var(--coral); color: #fff; font-family: "Rubik", sans-serif; font-weight: 600;
    font-size: 19px; line-height: 46px; text-align: center; z-index: 2;
  }
  .page-footer {
    position: absolute; left: 0; bottom: 0; width: 100%; height: 49px; background: var(--footer);
    color: var(--footer-text); padding: 16px 0 0 66px; font-size: 7.6px; line-height: 13px;
  }
</style>
</head>
<body>
<main class="spread">

  <article class="page page--left">
    <header class="page-header">
      <span class="brand">Boundless Stride</span>
      <span class="header-rule"></span>
      <span class="header-title">7 Keys to Achieving Success of Your RTLS Initiative</span>
    </header>

    <section class="key" style="top:96px">
      <div class="key-art" role="img" aria-label="Coral line illustration of a rocket launching"></div>
      <span class="key-label" style="top:10px">Key #3:</span>
      <h2 class="key-title" style="top:42px">Don’t Use Pilots to Test the RTLS Value</h2>
      <p class="key-text" style="top:90px">It is important to understand that RTLS technology has a certain threshold by which it becomes useful. So often, when new technologies are presented to our organizations, we tend to say: “Well, let’s do a little pilot, maybe in the ED or one clinic, and let’s see if this is really going to do all these things a vendor claims it will.” That’s not going to work for you with real-time location technologies because the true value comes when you can “light up” the entire organization. Unless you can “see” your entire system, you will be missing a whole lot of benefits RTLS technology can provide. Additionally, the technologies have reached a point of adoption that it is easy to find out how they have performed in the real-world from other organizations that have deployed them and have years of experience with using them.</p>
    </section>

    <section class="key" style="top:378px">
      <div class="key-art" role="img" aria-label="Coral line illustration of a set square, ruler and pencil"></div>
      <span class="key-label" style="top:10px">Key #4:</span>
      <h2 class="key-title" style="top:42px">Plan for the Future, from the Start</h2>
      <p class="key-text" style="top:88px">The Real-Time Technologies are becoming cheaper, faster, and better with each day. Therefore, you want to design your RTLS solution to accommodate this ongoing versatility and innovation. So don’t wed yourself to a company that offers one particular sensing technology or is very proprietary in nature. You want someone that can play nice with all the vendors and new technologies that are evolving in this space.</p>
    </section>

    <div class="page-number">02</div>
    <footer class="page-footer">© 2017 BOUNDLESS STRIDE, INC. ALL RIGHTS RESERVED.<br>www.boundlessstride.net</footer>
  </article>

  <article class="page page--right">
    <header class="page-header">
      <span class="brand">Boundless Stride</span>
      <span class="header-rule"></span>
      <span class="header-title">7 Keys to Achieving Success of Your RTLS Initiative</span>
    </header>

    <section class="key" style="top:97px">
      <div class="key-art" role="img" aria-label="Coral line illustration of a light bulb above a group of people"></div>
      <span class="key-label" style="top:10px">Key #5:</span>
      <h2 class="key-title" style="top:41px">Think about RTLS as an Initiative,<br>not a Project.</h2>
      <p class="key-text" style="top:105px">What surprises a lot of organizations as they begin to think about the Real-Time Technologies is that you’re going to need to create an RTLS team. Very often there is a desire to think that “we can just make my bio-med guy do this a couple hours a week and he’ll get some help from the IT folks, etc.” I can assure you – this is really not going to set you up to be successful. You need to have a dedicated team, sometimes even augmented by external experts, that can put the time and energy into rolling out this technology, making certain that it’s supported properly and continually maintained in a fashion that proves it to be reliable to the organization. Otherwise you’re going to have some real challenges in moving the initiative forward.</p>
    </section>

    <section class="key" style="top:383px">
      <div class="key-art" role="img" aria-label="Coral line illustration of a monitor showing adjustment sliders"></div>
      <span class="key-label" style="top:8px">Key #6:</span>
      <h2 class="key-title" style="top:40px">Nurture the Change</h2>
      <p class="key-text" style="top:85px">From my experience, the real challenge you’re going to have is the change management process – getting the people in your organization to embrace RTLS technology and use it to its maximum potential. That is going to take significant focus and work to be successful in that effort. You’re going to need to educate your staff on the role of RTLS, teach them how to use data to improve processes, and encourage them to stick to the new processes, when it is “just easier” to go back to the old ways of doing stuff.</p>
    </section>

    <div class="page-number">03</div>
    <footer class="page-footer">© 2017 BOUNDLESS STRIDE, INC. ALL RIGHTS RESERVED.<br>www.boundlessstride.net</footer>
  </article>

</main>
</body>
</html>
```